Ridgeway Business Card Redesign

Using the current logo/tagline lock-up and icon, redesign the Ridgeway business card to better show the tagline and improve the layout to give the card a more timely design and a classic, sophisticated look. See attached Project Brief for more detail.

```html
<!DOCTYPE html>
<html lang="en">
<head>
<meta charset="utf-8">
<title>Ridgeway Capital – Business Card</title>
<link href="https://fonts.googleapis.com/css2?family=Cinzel:wght@500;600&family=Tinos:ital@0;1&display=swap" rel="stylesheet">
<style>
  :root {
    --backdrop: #d6d6d6;
    --card: #ffffff;
    --ink: #1a1a1a;
    --ink-soft: #3f3f42;
    --brand-blue: #2a7fc9;
    --tree: #3a3a3c;
  }
  * { margin: 0; padding: 0; box-sizing: border-box; }
  html, body { width: 1200px; height: 960px; overflow: hidden; }
  body {
    background: var(--backdrop);
    position: relative;
    font-family: "Tinos", "Times New Roman", serif;
    color: var(--ink);
  }
  .card {
    position: absolute;
    left: 266px; top: 188px;
    width: 669px; height: 382px;
    background: var(--card);
    box-shadow: 0 4px 14px rgba(0,0,0,0.45);
  }
  .brand {
    position: absolute;
    display: flex; align-items: center;
  }
  .brand-dot { border-radius: 50%; background: var(--brand-blue); flex: none; }
  .brand-name {
    font-family: "Cinzel", serif;
    font-weight: 600;
    color: var(--ink-soft);
    line-height: 1;
    white-space: nowrap;
  }
  .card .brand { left: 24px; top: 28px; gap: 10px; }
  .card .brand-dot { width: 44px; height: 44px; }
  .card .brand-name { font-size: 17px; letter-spacing: 1px; }
  .tagline {
    position: absolute;
    font-family: "Cinzel", serif;
    font-weight: 600;
    color: var(--ink);
    white-space: nowrap;
    text-align: center;
  }
  .card .tagline { left: 0; width: 100%; top: 122px; font-size: 27px; letter-spacing: 0.3px; }
  .contact {
    position: absolute; left: 23px; top: 218px;
    font-size: 14.5px; line-height: 20px;
  }
  .contact .address { margin-bottom: 20px; }
  .contact .row span.label { display: inline-block; width: 62px; }
  .tree-art {
    position: absolute; left: 270px; top: 196px;
    width: 128px; height: 186px;
    background: linear-gradient(180deg, #ffffff 0%, #cfcfd0 40%, var(--tree) 100%);
  }
  .person {
    position: absolute; right: 25px; top: 292px;
    text-align: center;
  }
  .person .name { font-size: 19.5px; line-height: 24px; }
  .person .title { font-style: italic; font-size: 15px; line-height: 21px; }
  .showcase .brand { left: 266px; top: 712px; gap: 22px; }
  .showcase .brand-dot { width: 100px; height: 100px; }
  .showcase .brand-name { font-size: 42px; letter-spacing: 3px; }
  .showcase .tagline { left: 266px; width: 590px; top: 862px; font-size: 35px; }
</style>
</head>
<body>
  <section class="card">
    <div class="brand">
      <span class="brand-dot"></span>
      <span class="brand-name">Ridgeway Capital</span>
    </div>
    <h1 class="tagline">Non-Control Growth Capital</h1>
    <div class="contact">
      <p class="address">41 Linden Crest Road<br>Suite 210<br>Bethel, CT 06801</p>
      <p class="row"><span class="label">Office:</span>(555) 210-4471</p>
      <p class="row"><span class="label">Cell:</span>(555) 386-9025</p>
      <p class="row">dwhitcombe@ridgewaycapital.com</p>
    </div>
    <div class="tree-art" role="img" aria-label="Dark grey silhouette of a slender branching tree with star-shaped tufts"></div>
    <div class="person">
      <p class="name">Daniel R. Whitcombe</p>
      <p class="title">Principal &amp;<br>Chief Marketing Officer</p>
    </div>
  </section>
  <section class="showcase">
    <div class="brand">
      <span class="brand-dot"></span>
      <span class="brand-name">Ridgeway Capital</span>
    </div>
    <p class="tagline">Non-Control Growth Capital</p>
  </section>
</body>
</html>
```